Business Card for Dental Surgery

Professional and vibrant business card for dental surgery

Other side to incorporate space for appointment date and times

My website is www.larkvaledental.com.au

Target Market(s)

All

Industry/Entity Type

Dental

Requirements
Must have
• Catchy
Phone no, internet etc
Nice to have
• portray same image as website.
on reverse appointment side:
"Please give 24 hours notice if you cannot attend"
Nice colours

```html
<!DOCTYPE html>
<html lang="en">
<head>
<meta charset="utf-8">
<title>Larkvale Dental – Business Card</title>
<link href="https://fonts.googleapis.com/css2?family=Arimo:wght@400;700&display=swap" rel="stylesheet">
<style>
  :root {
    --page-bg: #e2e2e3;
    --card-bg: #ffffff;
    --purple: #9b2fae;
    --purple-light: #c25ad6;
    --green: #0bbf0b;
    --green-light: #22d61c;
    --ink: #6a6d73;
    --ink-soft: #7b7e84;
    --url: #8a4f96;
    --rule: #c9cbcf;
  }
  * { margin: 0; padding: 0; box-sizing: border-box; }
  html, body {
    width: 1200px;
    height: 765px;
    overflow: hidden;
    background: var(--page-bg);
    font-family: "Arimo", Arial, sans-serif;
  }
  .card {
    position: absolute;
    top: 302px;
    width: 575px;
    height: 343px;
    background: var(--card-bg);
    border-radius: 43px;
    overflow: hidden;
  }
  .card--front { left: 16px; }
  .card--back { left: 604px; }
  .card__band {
    position: absolute;
    left: 0; top: 0;
    width: 100%;
    height: 102px;
  }
  .card--front .card__band {
    background: radial-gradient(ellipse at 30% 40%, var(--purple-light), transparent 60%),
                radial-gradient(ellipse at 75% 30%, var(--purple-light), transparent 55%),
                var(--purple);
  }
  .card--back .card__band {
    background: radial-gradient(ellipse at 55% 20%, var(--green-light), transparent 60%),
                var(--green);
  }
  .band-note {
    position: absolute;
    left: 0; right: 0;
    top: 71px;
    text-align: center;
    color: #fff;
    font-size: 17px;
  }
  .band-note strong { font-weight: 700; }
  .brand {
    position: absolute;
    color: var(--purple);
    font-weight: 700;
    letter-spacing: -0.5px;
    white-space: nowrap;
  }
  .card--front .brand { left: 294px; top: 236px; font-size: 34px; }
  .card--back .brand { left: 70px; top: 205px; font-size: 23.5px; }
  .brand-url {
    position: absolute;
    left: 71px;
    top: 238px;
    font-size: 9.5px;
    letter-spacing: 2px;
    color: var(--url);
  }
  .appointment {
    position: absolute;
    left: 71px;
    top: 266px;
    width: 220px;
    color: var(--ink-soft);
  }
  .appointment__label {
    font-size: 10px;
    font-weight: 700;
    letter-spacing: 1px;
    text-transform: uppercase;
    color: var(--purple);
  }
  .appointment__field {
    display: flex;
    align-items: flex-end;
    gap: 8px;
    height: 20px;
    font-size: 11px;
  }
  .appointment__field span { width: 30px; }
  .appointment__line {
    flex: 1;
    border-bottom: 1px solid var(--rule);
    margin-bottom: 2px;
  }
  .contact {
    position: absolute;
    right: 68px;
    top: 165px;
    text-align: right;
    color: var(--ink);
  }
  .contact__name { font-size: 33px; font-weight: 700; line-height: 1; letter-spacing: 0.5px; }
  .contact__title { font-size: 16px; margin-top: 2px; color: var(--ink-soft); }
  .contact__list { list-style: none; margin-top: 14px; }
  .contact__item {
    display: flex;
    justify-content: flex-end;
    align-items: center;
    gap: 14px;
    height: 16px;
    font-size: 13px;
    color: var(--ink-soft);
  }
  .contact__item--email { font-size: 11px; }
  .contact__icon { width: 13px; height: 11px; fill: var(--purple); }
</style>
</head>
<body>
  <section class="card card--front">
    <div class="card__band"></div>
    <div class="brand">Larkvale Dental</div>
  </section>

  <section class="card card--back">
    <div class="card__band"></div>
    <p class="band-note">Please give <strong>24 hours</strong> notice if you cannot attend</p>
    <div class="brand">Larkvale Dental</div>
    <div class="brand-url">www.larkvaledental.com.au</div>

    <div class="appointment">
      <div class="appointment__label">Your next appointment</div>
      <div class="appointment__field"><span>Date</span><div class="appointment__line"></div></div>
      <div class="appointment__field"><span>Time</span><div class="appointment__line"></div></div>
    </div>

    <div class="contact">
      <div class="contact__name">JOHN DOE</div>
      <div class="contact__title">Job Title</div>
      <ul class="contact__list">
        <li class="contact__item">00 123 4567 890
          <svg class="contact__icon" viewBox="0 0 13 11"><path d="M1 3 Q6.5 -1 12 3 L10 5 L8.5 3.5 L4.5 3.5 L3 5 Z M3 6 H10 L11 10 H2 Z"/></svg>
        </li>
        <li class="contact__item">00 123 4567 890
          <svg class="contact__icon" viewBox="0 0 13 11"><path d="M3 0 H10 V3 H3 Z M1 4 H12 V8 H10 V6 H3 V8 H1 Z M3 7 H10 V11 H3 Z"/></svg>
        </li>
        <li class="contact__item">00 123 4567 890
          <svg class="contact__icon" viewBox="0 0 13 11"><path d="M2 0 H11 V11 H2 Z M4 2 V4 H9 V2 Z M4 6 V7 H5 V6 Z M6 6 V7 H7 V6 Z M8 6 V7 H9 V6 Z M4 8 V9 H5 V8 Z M6 8 V9 H7 V8 Z M8 8 V9 H9 V8 Z" fill-rule="evenodd"/></svg>
        </li>
        <li class="contact__item contact__item--email">john.doe@larkvaledental.com
          <svg class="contact__icon" viewBox="0 0 13 11"><path d="M1 1 H12 V10 H1 Z M1.5 1.5 L6.5 6 L11.5 1.5" fill-rule="evenodd"/></svg>
        </li>
      </ul>
    </div>
  </section>
</body>
</html>
```